Web Design Project

need a website, logo and a matching business Card for design studio. i have a company that works with many companies and i want to offer design services that will be outsourced to craftflock.

this website is totally for the design services. i need it to be simple but very catcgy and trendy, yet MUST BE ELEGENT.

you being a designer will know best what do i require in this website and how it should look and feel..

i dont need many pages, most of the selling work to clients will be face to face, this is just for them to view the sample works.

the company is called "Corvelin, Vividra Studio", so pages i need are: 1- the Studio 2- Folios 3- Contact us( will include company informaiton, and online contact form that should have a drop-down list of all types of designs.

main focus is the folios pages, it needs to have samples of works, the classification of works should be on two basis, by type of design and by designer. client should be able to select a certain designer and send an inquiry. if the customer does that, then i should get all client details and the designer should get a notification that he has been requested though no contact details of client should be given to designer as i want to make sure that those jobs are given to designer through craft flock and this is an invitation for any designer who care to put his works on the website. next to that, if the customer requires a job online then we need to get information on how design should feel and look.

please quote your price to include the website and business card design, A3 head letter and envelope.

Please provide a mock up of your design or a briefing an initial design before asking to be announced as the winner.

my customers are general managers and decision makers.

Business

• ability to filiter works based on type or designer. and website must offer all types of designs included here

```html
<!DOCTYPE html>
<html lang="en">
<head>
<meta charset="utf-8">
<title>Corvelin Studio</title>
<link rel="stylesheet" href="https://fonts.googleapis.com/css2?family=Arimo:wght@400;700&family=Handlee&display=swap">
<style>
:root{
  --page-blue:#3e6b93;
  --page-blue-dark:#35607f;
  --headline-blue:#3b6c95;
  --panel-blue:#4d93c8;
  --panel-blue-dark:#3f80b4;
  --orange:#f7811c;
  --orange-text:#f06d00;
  --text-dark:#333;
  --line:#e2e2e2;
  --white:#fff;
  --aqua:#3cc3d3;
  --aqua-light:#9fe7ef;
  --thumb-text:#d0d0d0;
}
*{box-sizing:border-box;margin:0;padding:0}
html,body{width:954px;height:1200px;overflow:hidden}
body{position:relative;background:var(--page-blue);font-family:"Arimo",Arial,sans-serif;color:var(--text-dark)}
.abs{position:absolute}

/* header */
.brand{left:113px;top:30px;height:34px;display:flex;align-items:center;gap:10px;color:var(--white);font-weight:700;font-size:26px;white-space:nowrap}
.brand-mark{width:16px;height:16px;background:var(--white)}
.btn-orange{background:linear-gradient(#ffa048,var(--orange));color:var(--white);border-radius:5px;box-shadow:0 2px 3px rgba(0,0,0,.25);display:flex;align-items:center;justify-content:center;font-size:14px;border:1px solid #e86f08}
.hire{left:667px;top:30px;width:175px;height:34px}

/* nav */
.nav{left:0;top:89px;width:954px;height:43px;background:linear-gradient(#fff,#f4f4f4 60%,#dcdcdc);box-shadow:0 2px 3px rgba(0,0,0,.2)}
.nav-item{top:0;height:43px;display:flex;align-items:center;justify-content:center;font-size:13px;color:#444}
.nav-divider{top:4px;width:1px;height:39px;background:#cfcfcf}
.nav-account{right:112px;top:0;height:43px;display:flex;align-items:center;gap:9px;font-size:10px;color:#555}

/* main panel */
.main{left:112px;top:138px;width:730px;height:941px;background:var(--white);border-radius:5px}
.hero{left:117px;top:143px;width:720px;height:196px;background:linear-gradient(#fff 50%,#e9e9e9);border-radius:3px;box-shadow:0 2px 4px rgba(0,0,0,.22)}
.hero-title{left:0;width:720px;top:26px;text-align:center;font-weight:700;font-size:31px;color:var(--headline-blue)}
.hero-steps{left:0;width:720px;top:78px;display:flex;justify-content:center;gap:20px;font-family:"Handlee",cursive;font-size:21px;color:#777}
.step{display:flex;align-items:center;gap:6px}
.btn-blue{background:linear-gradient(#5f8fb8,#3f6f98);color:var(--white);border-radius:4px;border:1px solid #35607f;box-shadow:0 2px 3px rgba(0,0,0,.25);display:flex;align-items:center;justify-content:center;font-size:14px}
.how{left:185px;top:141px;width:175px;height:34px}
.start{left:375px;top:141px;width:174px;height:34px}

/* services */
.service{top:375px;width:143px;height:104px;background:var(--white);border-radius:6px;box-shadow:0 1px 4px rgba(0,0,0,.3)}
.service-name{left:12px;top:13px;font-size:13.5px;font-weight:400;color:#222}
.service-from{left:14px;top:46px;font-size:13.5px;color:#888}
.service-price{left:14px;top:68px;font-size:13.5px;color:var(--headline-blue)}
.service-art{right:6px;top:38px;width:60px;height:56px;border-radius:8px}
.more{top:493px;width:60px;height:19px;border-radius:10px;background:linear-gradient(#fff,#dcdcdc);border:1px solid #b9b9b9;font-size:9.5px;font-weight:700;color:#444;display:flex;align-items:center;justify-content:center;box-shadow:0 1px 2px rgba(0,0,0,.2)}
.arrow{width:26px;height:40px}

/* listing panels */
.panel{background:var(--white);border-radius:5px;box-shadow:0 1px 4px rgba(0,0,0,.3);overflow:hidden}
.panel-head{height:27px;background:linear-gradient(var(--panel-blue),var(--panel-blue-dark));color:var(--white);font-size:13.5px;font-weight:400;padding-left:10px;line-height:27px}
.completed{left:153px;top:536px;width:302px;height:242px}
.open{left:489px;top:536px;width:303px;height:242px}
.col-head{top:38px;font-size:9.5px;font-weight:700;color:#333}
.row{left:10px;width:283px;height:43px;border-bottom:1px solid var(--line)}
.row-title{left:2px;top:10px;font-size:9.5px;font-weight:700;color:var(--orange-text)}
.row-desc{left:2px;top:27px;font-size:8.5px;color:#444}
.row-cell{top:15px;font-size:8.5px;font-weight:700;color:#333}
.btn-grey{height:33px;border-radius:5px;background:linear-gradient(#fff,#e7e7e7 70%,#d6d6d6);box-shadow:0 1px 3px rgba(0,0,0,.35);display:flex;align-items:center;justify-content:center;font-size:14px;color:#555}
.view-completed{left:156px;top:791px;width:302px}
.view-open{left:492px;top:791px;width:302px}

/* portfolios */
.portfolios{left:153px;top:846px;width:639px;height:207px}
.thumb{top:41px;width:147px;height:122px;border:1px solid #dcdcdc;display:flex;align-items:center;justify-content:center;font-size:21px;color:var(--thumb-text)}
.designer{top:176px;font-size:8.5px;font-weight:700;line-height:10px}
.designer-name{color:var(--orange-text)}
.designer-role{color:#333}

/* footer */
.footer{left:0;top:1095px;width:954px;height:105px;background:linear-gradient(#fff,#f2f2f2 60%,#dadada)}
.footer-brand{left:113px;top:41px;height:24px;display:flex;align-items:center;gap:8px;font-weight:700;font-size:18px;color:var(--headline-blue);white-space:nowrap}
.footer-mark{width:12px;height:12px;background:var(--headline-blue)}
.copyright{left:327px;top:49px;font-size:8.5px;color:#444}
.share{top:37px;width:90px;height:31px;border-radius:2px;display:flex;align-items:center;justify-content:center;gap:8px;font-size:13px;color:var(--white);letter-spacing:.5px;font-weight:700}
.share-one{left:649px;background:linear-gradient(#4d6ea8,#2f4f8a)}
.share-two{left:751px;background:linear-gradient(var(--aqua-light),var(--aqua))}
.share-square{width:14px;height:14px;background:rgba(255,255,255,.85)}
.bottom-band{left:0;top:1196px;width:954px;height:4px;background:var(--page-blue-dark)}
</style>
</head>
<body>

<header>
  <div class="abs brand"><span class="brand-mark"></span>Corvelin Studio</div>
  <a class="abs btn-orange hire">Hire this designer</a>
</header>

<nav class="abs nav">
  <svg class="abs" style="left:112px;top:12px" width="20" height="19" viewBox="0 0 20 19" aria-label="Home">
    <path d="M10 1 L19 9 H16 V18 H4 V9 H1 Z" fill="#3a8fd0"/>
    <rect x="8" y="11" width="4" height="7" fill="#f7811c"/>
  </svg>
  <span class="abs nav-divider" style="left:141px"></span>
  <a class="abs nav-item" style="left:141px;width:104px">The Studio</a>
  <span class="abs nav-divider" style="left:245px"></span>
  <a class="abs nav-item" style="left:245px;width:107px">Portfolios</a>
  <span class="abs nav-divider" style="left:352px"></span>
  <a class="abs nav-item" style="left:352px;width:136px">Browse Designs</a>
  <span class="abs nav-divider" style="left:488px"></span>
  <a class="abs nav-item" style="left:488px;width:130px">Contact Us</a>
  <div class="abs nav-account"><a>Login</a><span>|</span><a>Register</a></div>
</nav>

<main>
  <div class="abs main"></div>

  <section class="abs hero">
    <h1 class="abs hero-title">Lorem Ipsum Dolor. Lorem ipsum dolor.</h1>
    <div class="abs hero-steps">
      <span class="step"><svg width="34" height="28" viewBox="0 0 34 28"><path d="M2 14 L9 9 L14 16 L30 2 L33 5 L14 27 Z" fill="#4fc9d8" stroke="#2a9fb0"/></svg>Post a design</span>
      <span class="step"><svg width="34" height="28" viewBox="0 0 34 28"><path d="M2 14 L9 9 L14 16 L30 2 L33 5 L14 27 Z" fill="#4fc9d8" stroke="#2a9fb0"/></svg>Get Designs</span>
      <span class="step"><svg width="34" height="28" viewBox="0 0 34 28"><path d="M2 14 L9 9 L14 16 L30 2 L33 5 L14 27 Z" fill="#4fc9d8" stroke="#2a9fb0"/></svg>Hire Designer</span>
    </div>
    <a class="abs btn-blue how">See how it works</a>
    <a class="abs btn-orange start">Get started now</a>
  </section>

  <section class="services">
    <svg class="abs arrow" style="left:119px;top:410px" viewBox="0 0 26 40" aria-label="Previous"><path d="M20 3 L5 20 L20 37" fill="none" stroke="#f7811c" stroke-width="7" stroke-linecap="round" stroke-linejoin="round"/></svg>
    <svg class="abs arrow" style="left:808px;top:410px" viewBox="0 0 26 40" aria-label="Next"><path d="M6 3 L21 20 L6 37" fill="none" stroke="#f7811c" stroke-width="7" stroke-linecap="round" stroke-linejoin="round"/></svg>

    <article class="abs service" style="left:154px">
      <h3 class="abs service-name">Logo Design</h3>
      <p class="abs service-from">starting at</p><p class="abs service-price">$180</p>
      <div class="abs service-art" role="img" aria-label="Logo design illustration: letter and pen" style="background:linear-gradient(135deg,#e8eef5,#7fa6d6)"></div>
    </article>
    <article class="abs service" style="left:317px">
      <h3 class="abs service-name">Poster Design</h3>
      <p class="abs service-from">starting at</p><p class="abs service-price">$180</p>
      <div class="abs service-art" role="img" aria-label="Poster design illustration: paint palette and brush" style="background:linear-gradient(135deg,#f4e2b8,#d9a552)"></div>
    </article>
    <article class="abs service" style="left:485px">
      <h3 class="abs service-name">Web Design</h3>
      <p class="abs service-from">starting at</p><p class="abs service-price">$180</p>
      <div class="abs service-art" role="img" aria-label="Web design illustration: globe with brush" style="background:radial-gradient(circle at 40% 40%,#6ec3f2,#1c5fb0)"></div>
    </article>
    <article class="abs service" style="left:653px">
      <h3 class="abs service-name">Business Card</h3>
      <p class="abs service-from">starting at</p><p class="abs service-price">$180</p>
      <div class="abs service-art" role="img" aria-label="Business card illustration: stacked cards" style="background:linear-gradient(135deg,#eef3f0,#9fb7c4)"></div>
    </article>

    <a class="abs more" style="left:195px">More</a>
    <a class="abs more" style="left:358px">More</a>
    <a class="abs more" style="left:527px">More</a>
    <a class="abs more" style="left:696px">More</a>
  </section>

  <section class="abs panel completed">
    <h2 class="panel-head">Completed Designs</h2>
    <span class="abs col-head" style="left:12px">Project Title</span>
    <span class="abs col-head" style="left:145px">Budget</span>
    <span class="abs col-head" style="left:206px">Designs</span>
    <span class="abs col-head" style="left:262px">Winner</span>
    <div class="abs row" style="top:58px"><span class="abs row-title">Logo Design Project</span><span class="abs row-desc">Building designer logo required</span><span class="abs row-cell" style="left:142px">US$520</span><span class="abs row-cell" style="left:208px">166</span><span class="abs row-cell" style="left:248px">Ravindar</span></div>
    <div class="abs row" style="top:101px"><span class="abs row-title">Logo Design Project</span><span class="abs row-desc">Building designer logo required</span><span class="abs row-cell" style="left:142px">US$520</span><span class="abs row-cell" style="left:208px">166</span><span class="abs row-cell" style="left:248px">Ravindar</span></div>
    <div class="abs row" style="top:144px"><span class="abs row-title">Logo Design Project</span><span class="abs row-desc">Building designer logo required</span><span class="abs row-cell" style="left:142px">US$520</span><span class="abs row-cell" style="left:208px">166</span><span class="abs row-cell" style="left:248px">Ravindar</span></div>
    <div class="abs row" style="top:187px"><span class="abs row-title">Logo Design Project</span><span class="abs row-desc">Building designer logo required</span><span class="abs row-cell" style="left:142px">US$520</span><span class="abs row-cell" style="left:208px">166</span><span class="abs row-cell" style="left:248px">Ravindar</span></div>
  </section>

  <section class="abs panel open">
    <h2 class="panel-head">Open Designs</h2>
    <span class="abs col-head" style="left:12px">Project Title</span>
    <span class="abs col-head" style="left:145px">Budget</span>
    <span class="abs col-head" style="left:198px">Time Left</span>
    <div class="abs row" style="top:58px"><span class="abs row-title">Logo Design Project</span><span class="abs row-desc">Building designer logo required</span><span class="abs row-cell" style="left:142px">US$520</span><span class="abs row-cell" style="left:196px">11 days</span></div>
    <div class="abs row" style="top:101px"><span class="abs row-title">Logo Design Project</span><span class="abs row-desc">Building designer logo required</span><span class="abs row-cell" style="left:142px">US$520</span><span class="abs row-cell" style="left:196px">11 days</span></div>
    <div class="abs row" style="top:144px"><span class="abs row-title">Logo Design Project</span><span class="abs row-desc">Building designer logo required</span><span class="abs row-cell" style="left:142px">US$520</span><span class="abs row-cell" style="left:196px">11 days</span></div>
    <div class="abs row" style="top:187px"><span class="abs row-title">Logo Design Project</span><span class="abs row-desc">Building designer logo required</span><span class="abs row-cell" style="left:142px">US$520</span><span class="abs row-cell" style="left:196px">11 days</span></div>
  </section>

  <a class="abs btn-grey view-completed">View All Completed Designs</a>
  <a class="abs btn-grey view-open">View All Open Designs</a>

  <svg class="abs arrow" style="left:117px;top:927px" viewBox="0 0 26 40" aria-label="Previous"><path d="M20 3 L5 20 L20 37" fill="none" stroke="#f7811c" stroke-width="7" stroke-linecap="round" stroke-linejoin="round"/></svg>
  <svg class="abs arrow" style="left:804px;top:927px" viewBox="0 0 26 40" aria-label="Next"><path d="M6 3 L21 20 L6 37" fill="none" stroke="#f7811c" stroke-width="7" stroke-linecap="round" stroke-linejoin="round"/></svg>

  <section class="abs panel portfolios">
    <h2 class="panel-head">Top Designer Portfolios</h2>
    <div class="abs thumb" style="left:16px">Thumbnail</div>
    <div class="abs thumb" style="left:169px">Thumbnail</div>
    <div class="abs thumb" style="left:323px">Thumbnail</div>
    <div class="abs thumb" style="left:477px">Thumbnail</div>
    <p class="abs designer" style="left:17px"><span class="designer-name">Tidewell Co.</span><br><span class="designer-role">Logo Designer Canada</span></p>
    <p class="abs designer" style="left:170px"><span class="designer-name">Ravindar</span><br><span class="designer-role">Web Designer India</span></p>
    <p class="abs designer" style="left:324px"><span class="designer-name">Tidewell Co.</span><br><span class="designer-role">Logo Designer Canada</span></p>
    <p class="abs designer" style="left:478px"><span class="designer-name">Ravindar</span><br><span class="designer-role">Web Designer India</span></p>
  </section>
</main>

<footer class="abs footer">
  <div class="abs footer-brand"><span class="footer-mark"></span>Corvelin Studio</div>
  <p class="abs copyright">Copyright © 2012 Corvelin Studio. All Rights Reserved.</p>
  <a class="abs share share-one"><span class="share-square"></span>SHARE</a>
  <a class="abs share share-two"><span class="share-square"></span>SHARE</a>
</footer>
<div class="abs bottom-band"></div>

</body>
</html>
```